Motorcycle Shop Business Card

New business card for Motorcycle repair and customization shop.Business name: Copper Falcon Chris Morris443-865-5190, 7214 Quarry Lane Larkfield, MD 21904. www.dale@copperfalconcustoms.example. I uploaded some motorcycle images and logo and a couple of our calendar shoots. They do not have to be used on card just examples of some of our work and past graphic work.
We work on Vantor Brennick and Custom Built Motorcycles.

Looking for front and back design

Target Market(s)

Motorcycle owners

Industry/Entity Type

Motorcycle Part

```html
<!DOCTYPE html>
<html lang="en">
<head>
<meta charset="utf-8">
<title>Copper Falcon Customs – Business Card</title>
<link rel="stylesheet" href="https://fonts.googleapis.com/css2?family=Roboto:wght@400;700&display=swap">
<style>
  :root {
    --backdrop: #c9c9c9;
    --card-light: #a3a3a3;
    --card-dark: #7c7c7c;
    --ink: #111111;
    --paper: #ffffff;
    --rule: rgba(255,255,255,0.75);
    --ornament-dark: #2a2a2a;
  }
  * { margin: 0; padding: 0; box-sizing: border-box; }
  html, body { width: 1200px; height: 900px; overflow: hidden; }
  body {
    background: var(--backdrop);
    font-family: "Roboto", Arial, sans-serif;
    position: relative;
  }
  .card {
    position: absolute;
    width: 560px;
    height: 320px;
    border-radius: 22px;
    background: linear-gradient(160deg, var(--card-light) 0%, var(--card-dark) 100%);
    overflow: hidden;
    box-shadow: 0 14px 30px rgba(0,0,0,0.25);
  }
  .card-back { left: 90px; top: 110px; }
  .card-front { left: 550px; top: 470px; }

  .brand-box {
    position: absolute;
    background: var(--paper);
    border-radius: 16px;
    display: flex;
    align-items: center;
    justify-content: center;
    text-align: center;
  }
  .brand-name {
    color: var(--ink);
    font-weight: 700;
    line-height: 1.2;
    text-transform: uppercase;
    letter-spacing: 1px;
    white-space: nowrap;
  }

  .card-back .divider {
    position: absolute;
    left: 0; right: 0; top: 159px;
    height: 1px;
    background: var(--rule);
  }
  .card-back .brand-box { left: 190px; top: 105px; width: 180px; height: 110px; }
  .card-back .brand-name { font-size: 18px; }

  .card-front .brand-box { left: 150px; top: 24px; width: 160px; height: 100px; }
  .card-front .brand-name { font-size: 16px; }
  .card-front .brand-rule {
    position: absolute;
    left: 285px; top: 130px;
    width: 110px; height: 1px;
    background: var(--rule);
  }
  .holder-name {
    position: absolute;
    left: 30px; top: 140px;
    color: var(--paper);
    font-weight: 700;
    font-size: 20px;
    text-transform: uppercase;
    white-space: nowrap;
  }
  .holder-rule {
    position: absolute;
    left: 30px; top: 174px;
    width: 220px; height: 1px;
    background: var(--rule);
  }
  .contact-list {
    position: absolute;
    left: 30px; top: 188px;
    list-style: none;
    color: var(--paper);
    font-size: 17px;
  }
  .contact-list li {
    display: flex;
    align-items: center;
    gap: 12px;
    height: 32px;
    white-space: nowrap;
  }
  .contact-list svg { width: 14px; height: 14px; flex: none; }
  .ornament-area {
    position: absolute;
    left: 350px; top: 10px;
    width: 200px; height: 220px;
    border-radius: 24px;
    background: radial-gradient(circle at 55% 48%, var(--ornament-dark) 0%, rgba(42,42,42,0.55) 35%, rgba(255,255,255,0.18) 60%, rgba(255,255,255,0) 75%);
  }
</style>
</head>
<body>
  <section class="card card-back">
    <div class="divider"></div>
    <div class="brand-box"><span class="brand-name">Copper Falcon<br>Customs</span></div>
  </section>

  <section class="card card-front">
    <div class="brand-box"><span class="brand-name">Copper Falcon<br>Customs</span></div>
    <div class="brand-rule"></div>
    <div class="ornament-area" role="img" aria-label="Decorative cluster of black and white shapes"></div>
    <h1 class="holder-name">Copper Falcon Dale Fenwick</h1>
    <div class="holder-rule"></div>
    <ul class="contact-list">
      <li>
        <svg viewBox="0 0 16 16"><path d="M4 1.5l2.5 3-1.4 1.6a9 9 0 0 0 4.8 4.8l1.6-1.4 3 2.5-1.6 2.3C7.5 14 2 8.5 1.7 3.1z" fill="none" stroke="#fff" stroke-width="1.4"/></svg>
        <span>410-555-0137</span>
      </li>
      <li>
        <svg viewBox="0 0 16 16" fill="none" stroke="#fff" stroke-width="1.2"><circle cx="8" cy="8" r="6.5"/><ellipse cx="8" cy="8" rx="3" ry="6.5"/><path d="M1.5 8h13M2.5 4.8h11M2.5 11.2h11"/></svg>
        <span>www.dale@copperfalconcustoms.example</span>
      </li>
      <li>
        <svg viewBox="0 0 16 16"><path d="M8 15s5-5.2 5-9A5 5 0 0 0 3 6c0 3.8 5 9 5 9z" fill="#fff"/><circle cx="8" cy="6" r="1.8" fill="#8a8a8a"/></svg>
        <span>7214 Quarry Lane Larkfield, MD 21904</span>
      </li>
    </ul>
  </section>
</body>
</html>
```